Income Tax and Accounting Brochure

I need a brochure using my new logo (file attached). I do tax work and accounting work. I am an EA (QVX Enrolled Agent - logo attached) and would like this incorporated into the brochure. I also have a MSA in Accounting. Please incorporate the text that I have provided in the brochure.
Updates

Need extra days to review

Target Market(s)

Tax Clients - both business and individuals

Industry/Entity Type

Accounting

Colors
0054AA
0677BA
7BADD7
CADEEF
E8F1F8

Requirements
Must have
• Use my logo and the QVX EA file in the brochure
Nice to have
• I would like to see a brochure that I can customize with my own text if possible.

```html
<!DOCTYPE html>
<html lang="en">
<head>
<meta charset="utf-8">
<title>Harlow Accounting &amp; Consulting – About</title>
<link rel="stylesheet" href="https://fonts.googleapis.com/css2?family=Montserrat:wght@600;700&family=Roboto:wght@400&family=Roboto+Condensed:wght@400&display=swap">
<style>
  :root {
    --page: #ffffff;
    --card-light: #f2f1ef;
    --card-mid: #e6e4e1;
    --crimson: #d8073f;
    --crimson-deep: #b80c35;
    --navy: #2b3990;
    --royal: #0054aa;
    --sky: #1e7fc6;
    --ink: #2a2a2a;
    --badge-line: #8f8a62;
    --logo-navy: #1f3d8c;
  }
  * { margin: 0; padding: 0; box-sizing: border-box; }
  html, body { width: 876px; height: 1200px; overflow: hidden; background: var(--page); }
  .canvas { position: relative; width: 876px; height: 1200px; }
  .artwork { position: absolute; inset: 0; width: 876px; height: 1200px; }

  .ea-badge {
    position: absolute; left: 593px; top: 652px; width: 167px; height: 38px;
    border: 3px solid var(--badge-line); background: #efeee9;
  }
  .about-heading {
    position: absolute; right: 116px; top: 706px;
    font: 700 50px/1 "Montserrat", sans-serif; color: var(--sky); letter-spacing: 0.5px;
  }
  .principal-name {
    position: absolute; right: 116px; top: 755px;
    font: 400 34px/1 "Roboto", sans-serif; color: var(--crimson-deep);
  }
  .principal-title {
    position: absolute; left: 593px; top: 786px; width: 167px; height: 23px;
    background: var(--crimson-deep); color: #fff; text-align: right; padding-right: 2px;
    font: 400 19px/23px "Roboto Condensed", sans-serif;
  }
  .about-copy {
    position: absolute; left: 479px; top: 827px; width: 292px;
    font: 400 15.3px/18.9px "Roboto Condensed", sans-serif; color: var(--ink);
  }
  .about-copy p + p { margin-top: 4px; }

  .brand { position: absolute; left: 92px; top: 960px; }
  .brand-mark {
    position: absolute; left: 0; top: 0; width: 82px; height: 82px; border-radius: 50%;
    background: var(--logo-navy);
  }
  .brand-name {
    position: absolute; left: 98px; top: 10px; width: 260px;
    font: 600 21px/1.35 "Montserrat", sans-serif; color: var(--logo-navy); letter-spacing: 1px;
  }
  .brand-web {
    position: absolute; left: 101px; top: 94px;
    font: 400 15.5px/1 "Roboto", sans-serif; color: var(--crimson-deep); letter-spacing: 1.6px;
  }
</style>
</head>
<body>
<main class="canvas">
  <svg class="artwork" viewBox="0 0 1389 1920" preserveAspectRatio="none" xmlns="http://www.w3.org/2000/svg">
    <defs>
      <linearGradient id="cardTone" x1="0" y1="0" x2="1" y2="1">
        <stop offset="0" stop-color="#ecebe8"/>
        <stop offset="0.6" stop-color="#f3f2f0"/>
        <stop offset="1" stop-color="#e9e8e6"/>
      </linearGradient>
      <linearGradient id="photoTone" x1="0" y1="0" x2="0.6" y2="1">
        <stop offset="0" stop-color="#1c2538"/>
        <stop offset="0.45" stop-color="#4a5266"/>
        <stop offset="0.8" stop-color="#c9ccd2"/>
        <stop offset="1" stop-color="#e4e5e8"/>
      </linearGradient>
      <linearGradient id="mosaicTone" x1="0" y1="0" x2="1" y2="0.4">
        <stop offset="0" stop-color="#d8073f"/>
        <stop offset="0.3" stop-color="#2b3990"/>
        <stop offset="0.55" stop-color="#c20c38"/>
        <stop offset="0.8" stop-color="#1e7fc6"/>
        <stop offset="1" stop-color="#d8073f"/>
      </linearGradient>
    </defs>
    <rect class="card" x="73" y="75" width="1242" height="1755" fill="url(#cardTone)"/>
    <polygon class="hero-photo" role="img" aria-label="Photo: hands with a pen working on a calculator over paperwork"
      points="73,75 1313,75 1313,210 588,932 73,442" fill="url(#photoTone)"/>
    <polygon class="mosaic-band" role="img" aria-label="Geometric mosaic of red and blue triangles"
      points="73,462 588,975 1313,255 1313,665 487,1493 73,1080" fill="url(#mosaicTone)"/>
  </svg>

  <div class="ea-badge" aria-label="Enrolled agent badge"></div>

  <h1 class="about-heading">About</h1>
  <h2 class="principal-name">Marian D Holloway</h2>
  <div class="principal-title">MSA EA (Principal)</div>

  <section class="about-copy">
    <p>I have a Masters' Degree in accounting and am an QVX Enrolled Agent. I am also a LedgerBooks Advanced Certified Consultant in both the online and desktop products including Enterprise and Point of Sale.<br>I provide individual and small business tax services, Accounting, bookkeeping, QVX representation, insurance audit representation, business license assistance and more.</p>
    <p>I have experience working with a wide variety of clients from the point where they first decide they want to start a business. They are often unsure about what to do first- I have a lot of experience to offer you.</p>
  </section>

  <div class="brand">
    <div class="brand-mark"></div>
    <div class="brand-name">HARLOW ACCOUNTING &amp; CONSULTING, LLC</div>
    <div class="brand-web">www.harlowaccounting.com</div>
  </div>
</main>
</body>
</html>
```